BAG DESIGN / LAYOUT (cement bag for construction industry)

We need a new bag design as per the powerpoint draft. We are in the construction business and end up on jobsites. The idea is to have a bag on which the operator can easily cross the reference of the product with a marker (1 bag for all our products). Therefore we include the different options on the front of the bag (one list of the different systems we sell, one list of the different colors). We left blank for custom products and colors. Color restriction of the design bag: blue and tones of gray. There could be another color on the general design of the bag. But not more.

Target Market(s)

Contractors

Colors

Designer to choose only greyscale colors for use in the design.

Requirements
Must have
• We must have our logo stand out strongly. Color code possible. The bag can also be determined. We do not wish white too easely dirty. It could be in tones of gray, but you can surprise us with different colors
Nice to have
• A bad that stands out, and that has some character / personality.

```html
<!DOCTYPE html>
<html lang="fr">
<head>
<meta charset="utf-8">
<title>Meridia Concrete – Sac chantier</title>
<link rel="stylesheet" href="https://fonts.googleapis.com/css2?family=Archivo+Black&family=Merriweather:wght@700&family=Bebas+Neue&family=Alegreya+Sans+SC&family=Alegreya&display=swap">
<style>
  :root {
    --paper: #e1e1e1;
    --band-grey: #acacac;
    --brand-blue: #0057a8;
    --mark-blue: #0a5289;
    --charcoal: #232323;
    --strip: #c8c8c8;
    --fold: #111111;
    --white: #ffffff;
    --ink-light: #eeeeee;
    --alert-red: #e0343c;
    --label-grey: #9a9a9a;
  }
  * { margin: 0; padding: 0; box-sizing: border-box; }
  html, body { width: 1200px; height: 1004px; overflow: hidden; background: var(--white); }
  .bag { position: relative; width: 1200px; height: 1004px; overflow: hidden; }
  .bag-structure { position: absolute; inset: 0; }

  .wordmark {
    position: absolute; left: 222px; width: 456px; top: 278px;
    text-align: center; font-family: "Archivo Black", sans-serif;
    font-size: 35px; letter-spacing: 1px; color: var(--mark-blue);
  }
  .section-title {
    position: absolute; top: 444px; font-family: "Archivo Black", sans-serif;
    font-size: 23px; color: var(--white); letter-spacing: .5px;
  }
  .title-procede { left: 245px; }
  .title-teinte { left: 459px; }

  .tick-box { position: absolute; width: 28px; height: 26px; border: 1.5px solid var(--white); }
  .option-label {
    position: absolute; font-family: "Merriweather", serif; font-weight: 700;
    font-size: 9.3px; line-height: 11px; color: var(--white);
  }
  .custom-field { position: absolute; left: 283px; top: 607px; width: 143px; height: 26px; border: 1px solid var(--white); }

  .shade-table { position: absolute; width: 39px; border: 1px solid var(--white); }
  .shade-table div { height: 22px; border-bottom: 1px solid var(--white); }
  .shade-table div:last-child { border-bottom: 0; }
  .shade-label { position: absolute; font-family: "Merriweather", serif; font-weight: 700; font-size: 9.3px; color: var(--white); }

  .side-name {
    position: absolute; left: 714px; top: 434px; height: 216px; width: 22px;
    writing-mode: vertical-rl; font-family: "Archivo Black", sans-serif;
    font-size: 16px; color: var(--white); text-align: center; letter-spacing: .3px;
  }

  .origin {
    position: absolute; left: 243px; top: 695px; font-family: "Alegreya Sans SC", sans-serif;
    font-size: 20px; line-height: 22px; color: var(--alert-red);
  }
  .address {
    position: absolute; left: 242px; top: 778px; font-family: "Alegreya", serif;
    font-size: 16px; line-height: 22px; color: var(--ink-light); font-style: normal;
  }
  .weight-title {
    position: absolute; left: 517px; width: 120px; top: 686px; text-align: center;
    font-family: "Bebas Neue", sans-serif; font-size: 25px; letter-spacing: 6px; color: var(--white);
  }
  .weight-label { position: absolute; top: 716px; font-family: "Bebas Neue", sans-serif; font-size: 18px; color: var(--white); }
  .weight-box { position: absolute; width: 42px; height: 38px; border: 2.5px solid var(--brand-blue); }
  .hazard-code { position: absolute; top: 858px; font-family: "Merriweather", serif; font-weight: 700; font-size: 9px; color: var(--label-grey); }
</style>
</head>
<body>
<main class="bag">
  <svg class="bag-structure" width="1200" height="1004" viewBox="0 0 1200 1004" aria-hidden="true">
    <rect x="0" y="0" width="1200" height="399" fill="var(--paper)"/>
    <polygon points="0,140 426,139 345,267 0,272" fill="var(--band-grey)"/>
    <polygon points="485,139 1200,135 1200,270 565,270" fill="var(--brand-blue)"/>
    <rect x="0" y="399" width="1200" height="267" fill="var(--brand-blue)"/>
    <rect x="0" y="666" width="1200" height="10" fill="var(--strip)"/>
    <rect x="0" y="676" width="1200" height="263" fill="var(--charcoal)"/>
    <rect x="222" y="939" width="456" height="65" fill="var(--charcoal)"/>
    <g stroke="var(--fold)" stroke-width="2">
      <line x1="27" y1="2" x2="27" y2="939"/><line x1="27" y1="2" x2="92" y2="2"/>
      <line x1="92" y1="0" x2="92" y2="939"/>
      <line x1="222" y1="0" x2="222" y2="1004"/><line x1="222" y1="2" x2="678" y2="2"/>
      <line x1="678" y1="0" x2="678" y2="1004"/>
      <line x1="809" y1="0" x2="809" y2="937"/><line x1="678" y1="937" x2="809" y2="937"/>
      <line x1="0" y1="939" x2="222" y2="939"/><line x1="678" y1="939" x2="1200" y2="939"/>
    </g>
    <g stroke="#555" stroke-width=".7" stroke-dasharray="4 3">
      <line x1="156" y1="0" x2="156" y2="1004"/>
      <line x1="744" y1="0" x2="744" y2="1004"/>
    </g>
  </svg>

  <div class="wordmark">MERIDIA CONCRETE</div>

  <h2 class="section-title title-procede">PROCEDE</h2>
  <div class="tick-box" style="left:245px;top:497px"></div>
  <p class="option-label" style="left:281px;top:499px">Colorant<br>Durcisseur</p>
  <div class="tick-box" style="left:341px;top:497px"></div>
  <p class="option-label" style="left:376px;top:504px">Texture-</p>
  <div class="tick-box" style="left:245px;top:531px"></div>
  <p class="option-label" style="left:283px;top:538px">Sable</p>
  <div class="tick-box" style="left:341px;top:531px"></div>
  <p class="option-label" style="left:376px;top:539px">Niv’Sol</p>
  <div class="tick-box" style="left:245px;top:570px"></div>
  <p class="option-label" style="left:283px;top:576px">Microchape</p>
  <div class="tick-box" style="left:341px;top:570px"></div>
  <p class="option-label" style="left:376px;top:580px">wall Mix</p>
  <div class="tick-box" style="left:245px;top:607px"></div>
  <div class="custom-field"></div>

  <h2 class="section-title title-teinte">TEINTE</h2>
  <div class="shade-table" style="left:463px;top:496px"><div></div><div></div><div></div><div></div><div></div><div></div></div>
  <div class="shade-table" style="left:570px;top:496px"><div></div><div></div><div></div><div></div><div></div><div></div></div>
  <p class="shade-label" style="left:509px;top:500px">Pewter</p>
  <p class="shade-label" style="left:509px;top:523px">Acier</p>
  <p class="shade-label" style="left:509px;top:545px">Antracite</p>
  <p class="shade-label" style="left:509px;top:568px">Charbon</p>
  <p class="shade-label" style="left:509px;top:591px">Basalte</p>
  <p class="shade-label" style="left:509px;top:614px">Zinc</p>
  <p class="shade-label" style="left:617px;top:500px">Cappucino</p>
  <p class="shade-label" style="left:617px;top:523px">Bourgogne</p>
  <p class="shade-label" style="left:617px;top:545px">Sun Buff</p>
  <p class="shade-label" style="left:617px;top:568px">Blanc</p>
  <p class="shade-label" style="left:617px;top:591px">Cendra</p>
  <p class="shade-label" style="left:617px;top:614px">Rouge</p>

  <div class="side-name">MERIDIA CONCRETE</div>

  <p class="origin">Logo<br>Fabriqué à<br>la Réunion</p>
  <address class="address">MERIDIA CONCRETE SAS<br>12 Rue des Basaltes<br>97480 Anse-Sud – Réunion<br>www.meridiaconcrete.re</address>

  <h2 class="weight-title">POIDS</h2>
  <p class="weight-label" style="left:518px">25 KG</p>
  <p class="weight-label" style="left:597px">20 KG</p>
  <div class="weight-box" style="left:513px;top:744px"></div>
  <div class="weight-box" style="left:597px;top:744px"></div>

  <svg style="position:absolute;left:498px;top:797px" width="148" height="60" viewBox="0 0 148 60">
    <g role="img" aria-label="Pictogramme de danger irritant">
      <rect x="9" y="9" width="40" height="40" transform="rotate(45 29 29)" fill="var(--white)" stroke="var(--alert-red)" stroke-width="3"/>
      <rect x="27" y="16" width="4" height="17" rx="2" fill="var(--fold)"/>
      <circle cx="29" cy="39" r="2.5" fill="var(--fold)"/>
    </g>
    <g role="img" aria-label="Pictogramme de danger corrosif">
      <rect x="98" y="9" width="40" height="40" transform="rotate(45 118 29)" fill="var(--white)" stroke="var(--alert-red)" stroke-width="3"/>
      <rect x="106" y="21" width="24" height="14" fill="#bdbdbd"/>
    </g>
  </svg>
  <p class="hazard-code" style="left:513px">GHS07</p>
  <p class="hazard-code" style="left:601px">GHS05</p>
</main>
</body>
</html>
```